Business Card Design Project For Moving Company

Hello,

We need the business card to be 2 sided and we were thinking to use the logo on the front of the card (see file 1 attached) and the text "logo" (see file 2 attached) in the back of the card. We're looking for a powerful design that will help us build our brand, as our company is new.
We are a full service moving company (no storage) located in San Diego, CA, USA. The design should communicate to our potential customers that we have the highest level of service, customer satisfaction is our number one goal, our team is professional and efficient.

Thank you,

Gil
Updates

Project Deadline Extended
Reason: We would like to have more time to provide feedback for the designs already submitted. Thank you, Gil

Industry/Entity Type

Moving Company

Requirements
Must have
• Front of the card must have the following text and logo:
Haul Brightway, Inc
Residential And Commercial
Local And Long Distance
Address: 3917 Alder Crest Rd, #412,
San Diego, CA, 92087
P: 855-372-LIFT (5438)
F: 858-291-4476
info@haul-brightway.com
www.haul-brightway.com

Back of the card must have the following text and text "logo" (file 2 attached):

The best compliment we can ever receive is a referral from our clients.

```html
<!DOCTYPE html>
<html lang="en">
<head>
<meta charset="utf-8">
<title>Haul Brightway, Inc — Business Card</title>
<link rel="stylesheet" href="https://fonts.googleapis.com/css2?family=Fira+Sans+Condensed:ital,wght@0,600;1,400&family=Fira+Sans:wght@600&display=swap">
<style>
  :root {
    --paper: #ffffff;
    --ink: #111111;
    --brand-red: #ec1c24;
    --brand-red-deep: #b40a12;
    --band-black: #0d0d0d;
    --on-red: #ffffff;
  }
  * { margin: 0; padding: 0; box-sizing: border-box; }
  html, body { width: 1200px; height: 720px; overflow: hidden; background: var(--paper); }
  .card {
    position: relative;
    width: 1200px;
    height: 720px;
    background: var(--paper);
    overflow: hidden;
    font-family: "Fira Sans Condensed", "Arial Narrow", sans-serif;
  }
  .wave { position: absolute; inset: 0; width: 1200px; height: 720px; }

  .headline {
    position: absolute;
    color: var(--ink);
    font-style: italic;
    font-weight: 400;
    font-size: 44px;
    line-height: 1;
    white-space: nowrap;
  }
  .headline--company { left: 228px; top: 143px; }
  .headline--sectors { left: 224px; top: 210px; }
  .headline--range   { left: 220px; top: 276px; }

  .brand-name {
    position: absolute;
    right: 48px;
    top: 150px;
    width: 320px;
    text-align: right;
    color: var(--brand-red);
    font-style: italic;
    font-weight: 400;
    font-size: 76px;
    line-height: 0.95;
  }
  .brand-name span { display: block; }

  .contact {
    position: absolute;
    right: 816px;
    top: 496px;
    text-align: right;
    color: var(--on-red);
    font-style: italic;
    font-size: 23px;
    line-height: 33px;
    white-space: nowrap;
  }
  .contact__label {
    font-family: "Fira Sans", Arial, sans-serif;
    font-style: normal;
    font-weight: 600;
    font-size: 25px;
  }

  .web-line {
    position: absolute;
    left: 36px;
    top: 684px;
    color: var(--on-red);
    font-family: "Fira Sans", Arial, sans-serif;
    font-weight: 600;
    font-size: 23px;
    line-height: 1;
    white-space: nowrap;
  }
  .web-line__divider { margin: 0 18px; font-weight: 400; }
</style>
</head>
<body>
  <main class="card">
    <svg class="wave" viewBox="0 0 1100 660" preserveAspectRatio="none" aria-hidden="true">
      <defs>
        <linearGradient id="red-fill" x1="0" y1="0" x2="0" y2="1">
          <stop offset="0" stop-color="var(--brand-red)" style="stop-color:#ec1c24"/>
          <stop offset="1" stop-color="var(--brand-red-deep)" style="stop-color:#b40a12"/>
        </linearGradient>
      </defs>
      <path fill="#0d0d0d" d="M0 388 C 220 384, 420 420, 700 488 C 860 527, 990 548, 1100 556 L1100 660 L0 660 Z"/>
      <path fill="url(#red-fill)" d="M0 392 C 230 392, 430 432, 700 505 C 860 548, 990 590, 1100 606 L1100 660 L0 660 Z"/>
    </svg>

    <h1 class="headline headline--company">Haul Brightway, Inc</h1>
    <p class="headline headline--sectors">Residential And Commercial</p>
    <p class="headline headline--range">Local And Long Distance</p>

    <p class="brand-name"><span>Haul</span><span>Brightway</span></p>

    <address class="contact">
      <span class="contact__label">Address</span>: 3917 Alder Crest Rd, #412,<br>
      San Diego, CA, 92087<br>
      P: 855-372-LIFT (5438)<br>
      F: 858-291-4476
    </address>

    <p class="web-line">URL: www.haul-brightway.com<span class="web-line__divider">|</span>E-Mail: info@haul-brightway.com</p>
  </main>
</body>
</html>
```